Business cards for Champion Suri Alpaca Breeder

I am a seed stock Suri Alpaca breeder. I am looking for a business card design that is tactile with my logo or part of my logo embossed or debossed. I am open to other ideas.
My logo is available in detailed and simplified version. To get a feel for my style visit my website velmorfieldfleece.com

Target Market(s)

Alpaca breeders

Industry/Entity Type

Alpaca / Livestock

Contact Information for Business Card

Logo, Dora Plume, VELMORandFIELD.com, Marren Falls, OR 314-555-0172

Colors
0054AA
0677BA
7BADD7
CADEEF
E8F1F8

Requirements
Must have
• use brand guide
Nice to have
• embossed or debossed, incorporating a simple plaid use complimentary colors in logo
Should not have
• cartoon alpacas

```html
<!DOCTYPE html>
<html lang="en">
<head>
<meta charset="utf-8">
<title>Velmor &amp; Field — Business Cards</title>
<link href="https://fonts.googleapis.com/css2?family=Cinzel:wght@400;500&display=swap" rel="stylesheet">
<style>
  :root {
    --page: #d9d9d7;
    --cream-light: #fbf8ef;
    --cream-deep: #ede2cc;
    --ink: #141414;
    --frame-line: #f2ede2;
    --slate-top: #3d4b56;
    --slate-mid: #4b5b67;
    --slate-deep: #3a4853;
    --tan: #dcc3a6;
    --contact: #ece4d9;
    --sky: #7f95ad;
    --meadow: #6f8062;
  }
  * { box-sizing: border-box; margin: 0; padding: 0; }
  html, body { width: 1200px; height: 1200px; overflow: hidden; }
  body {
    background: var(--page);
    font-family: "Cinzel", serif;
    position: relative;
  }
  .card {
    position: absolute;
    top: 190px;
    width: 460px;
    height: 805px;
    box-shadow: 0 14px 34px rgba(0,0,0,0.25);
  }
  /* Front */
  .card--front {
    left: 110px;
    background: radial-gradient(ellipse at 45% 40%, var(--cream-light) 40%, var(--cream-deep) 100%);
  }
  .logo-frame {
    position: absolute;
    left: 65px; top: 150px;
    width: 330px; height: 500px;
    background: var(--ink);
    padding: 9px;
  }
  .logo-frame__inner {
    width: 100%; height: 100%;
    border: 1.5px solid var(--frame-line);
    padding: 5px;
    display: flex; flex-direction: column;
  }
  .logo-art {
    flex: 1;
    background: linear-gradient(180deg, var(--sky) 0%, #a9b7c6 45%, #8c8473 62%, var(--meadow) 100%);
  }
  .logo-name {
    height: 72px;
    display: flex; align-items: center; justify-content: center;
    color: #f6f1e6;
    font-size: 30px;
    font-weight: 400;
    letter-spacing: 1px;
    white-space: nowrap;
    border-top: 1.5px solid var(--frame-line);
    margin-top: 5px;
  }
  /* Back */
  .card--back {
    left: 630px;
    background: linear-gradient(160deg, var(--slate-top) 0%, var(--slate-mid) 50%, var(--slate-deep) 100%);
    color: var(--tan);
  }
  .rule {
    position: absolute;
    left: 60px; width: 340px; height: 20px;
  }
  .rule--top { top: 150px; }
  .rule--bottom { top: 625px; }
  .holder-name {
    position: absolute;
    left: 60px; top: 250px;
    font-size: 38px;
    font-weight: 400;
    letter-spacing: 2px;
    white-space: nowrap;
  }
  .contact-list {
    position: absolute;
    left: 60px; top: 330px;
    list-style: none;
  }
  .contact-list li {
    display: flex; align-items: center;
    height: 58px;
    font-size: 24px;
    color: var(--contact);
    letter-spacing: 1px;
    white-space: nowrap;
  }
  .contact-list svg {
    width: 28px; height: 28px;
    margin-right: 18px;
    flex: none;
  }
</style>
</head>
<body>

  <section class="card card--front">
    <div class="logo-frame">
      <div class="logo-frame__inner">
        <div class="logo-art" role="img" aria-label="Engraved-style illustration of an alpaca standing in a green meadow under a cloudy blue sky"></div>
        <div class="logo-name">VELMOR &amp; FIELD</div>
      </div>
    </div>
  </section>

  <section class="card card--back">
    <svg class="rule rule--top" viewBox="0 0 340 20" aria-hidden="true">
      <line x1="0" y1="10" x2="340" y2="10" stroke="var(--tan)" stroke-width="1.5"/>
      <rect x="164" y="4" width="12" height="12" transform="rotate(45 170 10)" fill="var(--tan)"/>
    </svg>

    <h1 class="holder-name">DORA PLUME</h1>

    <ul class="contact-list">
      <li>
        <svg viewBox="0 0 24 24" aria-hidden="true"><path fill="var(--tan)" d="M6.6 10.8a15 15 0 0 0 6.6 6.6l2.2-2.2a1 1 0 0 1 1-.25 11.4 11.4 0 0 0 3.6.57 1 1 0 0 1 1 1V20a1 1 0 0 1-1 1A17 17 0 0 1 3 4a1 1 0 0 1 1-1h3.5a1 1 0 0 1 1 1c0 1.25.2 2.45.57 3.57a1 1 0 0 1-.25 1z"/></svg>
        (314) 555-0172
      </li>
      <li>
        <svg viewBox="0 0 24 24" aria-hidden="true" fill="none" stroke="var(--tan)" stroke-width="1.6"><circle cx="12" cy="12" r="9.5"/><ellipse cx="12" cy="12" rx="4.5" ry="9.5"/><line x1="2.5" y1="12" x2="21.5" y2="12"/><path d="M4.5 7h15M4.5 17h15"/></svg>
        VELMORANDFIELD.COM
      </li>
      <li>
        <svg viewBox="0 0 24 24" aria-hidden="true"><path fill="var(--tan)" d="M12 2a7 7 0 0 0-7 7c0 5.2 7 13 7 13s7-7.8 7-13a7 7 0 0 0-7-7zm0 9.5A2.5 2.5 0 1 1 12 6.5a2.5 2.5 0 0 1 0 5z"/></svg>
        Marren Falls, OR
      </li>
    </ul>

    <svg class="rule rule--bottom" viewBox="0 0 340 20" aria-hidden="true">
      <line x1="0" y1="10" x2="340" y2="10" stroke="var(--tan)" stroke-width="1.5"/>
      <rect x="164" y="4" width="12" height="12" transform="rotate(45 170 10)" fill="var(--tan)"/>
    </svg>
  </section>

</body>
</html>
```